Brevik Fabrication - Business Card Design

We would like a dark (likely black) themed business card to be able to hand out to potential clients. We may list our services on the card or keep it clean. Unsure. Logo attached

```html
<!DOCTYPE html>
<html lang="en">
<head>
<meta charset="utf-8">
<title>Brevik Fabrication – Business Card</title>
<link rel="stylesheet" href="https://fonts.googleapis.com/css2?family=Josefin+Sans:wght@400;600&display=swap">
<style>
  :root {
    --backdrop: #78767b;
    --card-top: #161616;
    --card-mid: #0f0f0f;
    --card-bottom: #060606;
    --accent: #f06136;
    --ink-light: #ffffff;
    --ink-soft: #e6e6e6;
  }
  * { box-sizing: border-box; margin: 0; padding: 0; }
  html, body {
    width: 1199px; height: 1200px; overflow: hidden;
    background: var(--backdrop);
    font-family: "Josefin Sans", "Helvetica Neue", Arial, sans-serif;
  }
  .stage { position: relative; width: 1199px; height: 1200px; }
  .card {
    position: absolute; left: 331px; width: 538px; height: 309px;
    background: linear-gradient(180deg, var(--card-top) 0%, var(--card-mid) 55%, var(--card-bottom) 100%);
    overflow: hidden;
  }
  .card--front { top: 271px; }
  .card--back { top: 652px; }

  .front-shapes { position: absolute; inset: 0; width: 100%; height: 100%; }
  .shape-accent { fill: var(--accent); }
  .shape-stripe { fill: #080808; }

  .brand {
    position: absolute; left: 267px; top: 150px; transform: translate(-50%, -50%);
    display: flex; align-items: center; gap: 9px; white-space: nowrap;
  }
  .brand-dot { width: 14px; height: 14px; border-radius: 50%; background: var(--accent); flex: none; }
  .brand-name {
    font-size: 19px; font-weight: 600; color: var(--accent);
    letter-spacing: 0.5px; line-height: 1;
  }

  .identity {
    position: absolute; left: 134px; top: 127px; transform: translateX(-50%);
    text-align: center; white-space: nowrap;
  }
  .identity-name {
    font-size: 33px; font-weight: 400; color: var(--ink-light);
    letter-spacing: 0.3px; line-height: 1;
  }
  .identity-role {
    margin-top: 7px; font-size: 19px; font-weight: 400; color: var(--accent);
    letter-spacing: 5px; padding-left: 5px; line-height: 1;
  }

  .divider {
    position: absolute; left: 268px; top: 30px; width: 1px; height: 260px;
    background: linear-gradient(180deg, rgba(240,97,54,0) 0%, var(--accent) 50%, rgba(240,97,54,0) 100%);
  }

  .contacts { position: absolute; right: 26px; top: 130px; list-style: none; }
  .contact-item {
    display: flex; align-items: center; justify-content: flex-end; gap: 13px;
    height: 18px; margin-bottom: 17px;
    font-size: 13px; color: var(--ink-soft); letter-spacing: 0.3px; white-space: nowrap;
  }
  .contact-icon { width: 14px; height: 16px; flex: none; }
  .contact-icon * { fill: none; stroke: var(--accent); stroke-width: 1.2; }
</style>
</head>
<body>
<main class="stage">
  <section class="card card--front" aria-label="Card front">
    <svg class="front-shapes" viewBox="0 0 538 309" preserveAspectRatio="none" aria-hidden="true">
      <polygon class="shape-accent" points="264,309 475,38 538,46 538,309"/>
      <polygon class="shape-stripe" points="318,309 500,84 538,96 538,104 508,96 338,309"/>
    </svg>
    <div class="brand">
      <span class="brand-dot"></span>
      <span class="brand-name">Brevik Fabrication</span>
    </div>
  </section>

  <section class="card card--back" aria-label="Card back">
    <div class="identity">
      <p class="identity-name">YOUR NAME</p>
      <p class="identity-role">CEO</p>
    </div>
    <span class="divider"></span>
    <ul class="contacts">
      <li class="contact-item">
        <span>+1 (533) 402–7719</span>
        <svg class="contact-icon" viewBox="0 0 14 16" aria-hidden="true">
          <rect x="3.5" y="1" width="8" height="14" rx="1.2"/>
          <line x1="6.5" y1="12.8" x2="8.5" y2="12.8"/>
        </svg>
      </li>
      <li class="contact-item">
        <span>info@brevikfabrication.com</span>
        <svg class="contact-icon" viewBox="0 0 14 16" aria-hidden="true">
          <rect x="0.8" y="4" width="12.4" height="8.5"/>
          <polyline points="0.8,4 7,9 13.2,4"/>
        </svg>
      </li>
    </ul>
  </section>
</main>
</body>
</html>
```